U.S. based testing, inspection, and certification (TIC) company needs a new PowerPoint template.

We need a new PowerPoint template (deck, slide deck) for our U.S. based company with international capabilities for performing numerous testing, inspection, and certification (TIC) services. Our primary services include calibration, chemical analysis, consulting engineering, environmental simulation, forensic engineering, materials testing, mechanical testing, and nondestructive testing. Industries we serve are aerospace/aviation, automotive, chemical, commercial properties, construction, consumer products, defense, energy storage, healthcare, insurance/legal, life science, manufacturing, oil & gas, power generation, pulp & paper, and telecommunications. https://qirvotest.com/

Guideline hex colors: #29aae2, #0b1f3b, #fb6805 (use orange more subtly)

The final design should communicate:
1. Trust, Integrity, and Independence
2. Technical Expertise and Accuracy
3. Efficiency and Speed
4. Value-Added Partnership

Our current branding reflects a variety of styles, several of which have been included as attachments for reference in this project. While these examples showcase the direction we have taken in the past, we are not limited to them and remain open to exploring fresh, innovative design that is simple, clean, and with plenty of space to add content for each slide. We welcome creative concepts that build on or reimagine our existing identity to better align with our evolving vision.

```html
<!DOCTYPE html>
<html lang="en">
<head>
<meta charset="utf-8">
<title>Qirvo Testing Services – Presentation Template</title>
<link href="https://fonts.googleapis.com/css2?family=Roboto:ital,wght@0,300;0,400;0,500;0,700;1,300;1,400&display=swap" rel="stylesheet">
<style>
  :root{
    --navy:#0b1f3b;
    --navy-deep:#081a33;
    --blue:#29aae2;
    --blue-strong:#1689d8;
    --orange:#fb6805;
    --ink:#0b1f3b;
    --text:#222b38;
    --rule:#d5dbe3;
    --stage:#3a3a3a;
    --white:#ffffff;
  }
  *{box-sizing:border-box;margin:0;padding:0}
  html,body{width:924px;height:1200px;overflow:hidden;background:var(--stage)}
  body{position:relative;font-family:'Roboto',Arial,sans-serif;color:var(--text)}
  .slide{position:absolute;overflow:hidden;background:var(--white)}
  .slide.dark{background:var(--navy)}
  .abs{position:absolute}
  .badge{position:absolute;top:0;width:17px;height:21px;background:var(--blue-strong);color:var(--white);
    font-weight:700;font-size:10.5px;display:flex;align-items:center;justify-content:center;
    clip-path:polygon(0 0,100% 0,100% 82%,80% 100%,0 100%)}
  .title{position:absolute;font-weight:700;color:var(--ink);font-size:15.5px;letter-spacing:.1px;line-height:1.1;white-space:nowrap}
  .subtitle{position:absolute;color:var(--blue-strong);font-size:9.5px;font-weight:500;line-height:1.2;white-space:nowrap}
  .accent{position:absolute;height:1.2px;background:var(--orange)}
  .body{position:absolute;font-size:4.6px;line-height:1.25;color:var(--text)}
  .art{position:absolute}

  /* Cover */
  .cover{left:90px;top:54px;width:744px;height:419px;background:var(--navy-deep)}
  .cover .wordmark{position:absolute;left:57px;top:60px;color:var(--white);font-weight:700;font-size:27px;line-height:1;letter-spacing:.5px}
  .cover .wordmark small{display:block;font-size:11.5px;font-weight:700;letter-spacing:.2px;margin-top:6px}
  .cover .headline{position:absolute;left:55px;top:155px;color:var(--white);font-weight:700;font-size:21.5px;line-height:1.2}
  .cover .headline span{color:var(--blue-strong)}
  .cover .tagline{position:absolute;left:55px;top:267px;color:var(--white);font-weight:300;font-size:14.5px;line-height:1.25}
  .cover .rule{position:absolute;left:55px;width:233px;height:.6px;background:var(--orange)}
  .cover .reach{position:absolute;left:55px;top:331px;display:flex;align-items:center;gap:9px;color:var(--white);font-style:italic;font-weight:300;font-size:14.5px;line-height:1.1}

  /* Lists */
  .values li{position:absolute;list-style:none;display:flex;align-items:center;gap:8px;font-size:5.4px;font-weight:500;color:var(--ink)}
  .values svg,.services svg{width:10px;height:10px;flex:none}
  .services li{position:absolute;list-style:none;display:flex;align-items:center;gap:5px;font-size:5.5px;color:var(--ink);
    width:76px;padding-bottom:3px;border-bottom:.5px solid var(--rule)}
  .note{position:absolute;font-size:5px;font-weight:500;color:var(--ink);line-height:1.15;padding-left:4px;border-left:1.2px solid var(--blue-strong)}
  .dots{position:absolute;width:34px;height:6px;background-image:radial-gradient(circle,#c6cdd6 .6px,transparent .8px);background-size:5px 3px}

  /* Training */
  .hexlabel{font-size:5.2px;font-weight:500;fill:var(--white);text-anchor:middle}
  .location{position:absolute;left:0;top:166px;width:85px;height:21px;background:var(--blue-strong);color:var(--white);font-weight:500;font-size:8.5px;
    display:flex;align-items:center;padding-left:25px;clip-path:polygon(0 0,88% 0,100% 50%,88% 100%,0 100%)}
  .loc-item{position:absolute;top:169px;display:flex;align-items:center;gap:3px;color:var(--white);font-weight:500;font-size:6.5px;line-height:1}
  .loc-item small{display:block;font-size:3.6px;font-weight:400}

  /* Industries */
  .industry{position:absolute;width:46px;text-align:center;font-size:4.4px;color:var(--ink);line-height:1.15}
  .industry svg{display:block;margin:0 auto 3px;width:17px;height:17px}
  .vline{position:absolute;width:.5px;background:var(--rule)}

  /* Reasons */
  .reason{position:absolute;left:28px;display:flex;gap:6px;width:190px;padding-bottom:3px;border-bottom:.5px solid var(--rule)}
  .reason svg{width:13px;height:13px;flex:none}
  .reason h3{font-size:6.5px;font-weight:500;color:var(--blue-strong);line-height:1.1}
  .reason p{font-size:4.2px;color:var(--text);line-height:1.15}

  /* Closing */
  .benefit{position:absolute;top:139px;width:54px;text-align:center;font-size:5px;color:var(--ink);line-height:1.15}
  .benefit svg{display:block;margin:0 auto 3px;width:14px;height:14px}
  .contact{position:absolute;left:0;top:172px;width:85px;height:20px;background:var(--navy);color:var(--white);font-weight:700;font-size:8.5px;
    display:flex;align-items:center;padding-left:20px;clip-path:polygon(0 0,92% 0,100% 50%,92% 100%,0 100%)}
  .contact-edge{position:absolute;left:0;top:172px;width:88px;height:20px;background:var(--blue-strong);clip-path:polygon(0 0,92% 0,100% 50%,92% 100%,0 100%)}
  .contact-item{position:absolute;top:175px;display:flex;align-items:center;gap:3px;font-weight:700;font-size:6.5px;color:var(--ink);line-height:1}
  .contact-item small{display:block;font-size:3.6px;font-weight:400}
</style>
</head>
<body>

<!-- 01 Cover -->
<section class="slide cover">
  <svg class="art" style="left:0;top:0" width="744" height="419" viewBox="0 0 744 419">
    <defs>
      <linearGradient id="labPhoto" x1="0" y1="0" x2="0.6" y2="1">
        <stop offset="0" stop-color="#d7735a"/>
        <stop offset=".22" stop-color="#a9b4c4"/>
        <stop offset=".55" stop-color="#8797b0"/>
        <stop offset="1" stop-color="#22417a"/>
      </linearGradient>
    </defs>
    <polygon points="448,0 744,0 744,419 355,419" fill="url(#labPhoto)" role="img" aria-label="Close-up photo of laboratory microscope objectives over a sample slide"/>
    <polygon points="470,269 597,269 561,419 435,419" fill="var(--blue-strong)"/>
    <polygon points="597,269 640,269 604,419 561,419" fill="#1c7cc9" opacity=".7"/>
    <polygon points="744,174 744,419 709,419" fill="var(--blue-strong)"/>
    <polygon points="744,110 744,174 700,419 678,419" fill="var(--navy-deep)"/>
  </svg>
  <div class="wordmark">Qirvo<small>Qirvo Testing Services</small></div>
  <h1 class="headline">YOUR TRUSTED PARTNER<br>IN <span>TESTING, INSPECTION</span><br><span>&amp; CERTIFICATION</span></h1>
  <div class="accent" style="left:55px;top:249px;width:69px;height:1.6px"></div>
  <p class="tagline">Delivering Confidence Through Precision,<br>Innovation, and Independent Expertise</p>
  <div class="rule" style="top:325px"></div>
  <div class="reach">
    <svg width="30" height="30" viewBox="0 0 30 30" fill="none" stroke="#fff" stroke-width="1">
      <circle cx="13" cy="14" r="12"/><ellipse cx="13" cy="14" rx="5" ry="12"/><line x1="1" y1="14" x2="25" y2="14"/>
      <line x1="3" y1="8" x2="23" y2="8"/><line x1="3" y1="20" x2="18" y2="20"/>
      <line x1="24" y1="28" x2="24" y2="17"/><polyline points="21,20 24,17 27,20"/>
    </svg>
    <span>Trusted Solutions Across<br>Critical Industries Worldwide</span>
  </div>
  <div class="rule" style="top:371px"></div>
</section>

<!-- 02 Who we are -->
<section class="slide" style="left:90px;top:490px;width:362px;height:203px">
  <div class="badge" style="left:24px">02</div>
  <h2 class="title" style="left:25px;top:44px">WHO WE ARE</h2>
  <p class="subtitle" style="left:25px;top:63px;font-size:10.5px">Independent Expertise.<br>Global Capability.</p>
  <div class="accent" style="left:25px;top:93px;width:33px"></div>
  <p class="body" style="left:25px;top:102px;width:110px">For decades, we have helped organizations verify performance, ensure compliance, and reduce risk through comprehensive testing, inspection, engineering, and certification services.</p>
  <p class="body" style="left:25px;top:130px;width:110px">Our multidisciplinary teams combine advanced technology with deep technical knowledge to provide objective, accurate, and timely results that support confident decision-making.</p>
  <div class="vline" style="left:168px;top:40px;height:127px;background:#c9d0d8"></div>
  <ul class="values">
    <li style="left:200px;top:52px"><svg viewBox="0 0 10 10" fill="none" stroke="#0b1f3b" stroke-width=".7"><path d="M5 .8 8.8 2.2V5C8.8 7.3 5 9.2 5 9.2S1.2 7.3 1.2 5V2.2Z"/><path d="M5 3.5v3M3.5 5h3"/></svg>Integrity in every evaluation</li>
    <li style="left:200px;top:75px"><svg viewBox="0 0 10 10" fill="none" stroke="#0b1f3b" stroke-width=".7"><circle cx="5" cy="5" r="3.6"/><path d="M5 0v2.5M5 7.5V10M0 5h2.5M7.5 5H10"/></svg>Technical excellence backed by experience</li>
    <li style="left:200px;top:98px"><svg viewBox="0 0 10 10" fill="none" stroke="#0b1f3b" stroke-width=".7"><path d="M5 1v8M2 9h6M1 3h8M2.5 3 1 6h3ZM7.5 3 6 6h3Z"/></svg>Independent and unbiased reporting</li>
    <li style="left:200px;top:121px"><svg viewBox="0 0 10 10" fill="none" stroke="#0b1f3b" stroke-width=".7"><circle cx="3" cy="2.5" r="1"/><circle cx="7" cy="2.5" r="1"/><circle cx="5" cy="4.5" r="1"/><path d="M1 8c0-2 4-2 4 0M5 8c0-2 4-2 4 0"/></svg>Customer-focused collaboration</li>
    <li style="left:200px;top:144px"><svg viewBox="0 0 10 10" fill="none" stroke="#0b1f3b" stroke-width=".8"><circle cx="5" cy="4" r="2.8"/><path d="M3 6.5 2 9.5M7 6.5 8 9.5"/></svg>Commitment to quality and safety</li>
  </ul>
  <div class="dots" style="left:290px;top:180px"></div>
  <div class="abs" style="left:0;top:197px;width:122px;height:6px;background:var(--blue-strong);clip-path:polygon(0 0,96% 0,100% 100%,0 100%)"></div>
</section>

<!-- 03 Core services -->
<section class="slide" style="left:472px;top:490px;width:362px;height:203px">
  <svg class="art" style="left:0;top:0" width="362" height="203" viewBox="0 0 362 203">
    <defs>
      <linearGradient id="techPhoto" x1="0" y1="0" x2="1" y2="1">
        <stop offset="0" stop-color="#c4ccd6"/><stop offset=".5" stop-color="#5c7290"/><stop offset="1" stop-color="#1b3358"/>
      </linearGradient>
    </defs>
    <polygon points="297,0 362,0 362,203 300,203 258,87" fill="#d8dde3"/>
    <polygon points="302,0 362,0 362,190 305,180 264,87" fill="url(#techPhoto)" role="img" aria-label="Photo of an engineer in safety glasses working in a testing facility"/>
    <polygon points="269,203 362,203 362,111" fill="var(--blue-strong)"/>
  </svg>
  <div class="badge" style="left:28px">03</div>
  <h2 class="title" style="left:28px;top:30px">OUR CORE SERVICES</h2>
  <p class="subtitle" style="left:28px;top:46px">Comprehensive Technical Solutions</p>
  <ul class="services">
    <li style="left:28px;top:72px"><svg viewBox="0 0 10 10" fill="none" stroke="#0b1f3b" stroke-width=".7"><path d="M2 1v8M5 1v8M8 1v8"/><path d="M1 3h2M4 6h2M7 4h2"/></svg>Calibration Services</li>
    <li style="left:28px;top:90px"><svg viewBox="0 0 10 10" fill="none" stroke="#0b1f3b" stroke-width=".7"><path d="M4 1h2M4.3 1v3L1.5 9h7L5.7 4V1"/></svg>Chemical Analysis</li>
    <li style="left:28px;top:109px"><svg viewBox="0 0 10 10" fill="none" stroke="#29aae2" stroke-width=".7"><path d="M2 9h6M3 9 5 5l3-2M6 2l2 1"/></svg>Consulting Engineering</li>
    <li style="left:28px;top:127px"><svg viewBox="0 0 10 10" fill="none" stroke="#0b1f3b" stroke-width=".7"><rect x="1.5" y="1.5" width="6" height="7"/><path d="M3 4h3M3 6h3"/><circle cx="8" cy="8" r="1.2" stroke="#29aae2"/></svg>Environmental Simulation</li>
    <li style="left:28px;top:146px;border-bottom:none"><svg viewBox="0 0 10 10" fill="none" stroke="#29aae2" stroke-width=".7"><path d="M2 1h6M2 9h6M3 1c0 3 4 3 4 4s-4 1-4 4M7 1c0 3-4 3-4 4"/></svg>Forensic Engineering</li>
    <li style="left:128px;top:72px;width:110px"><svg viewBox="0 0 10 10" fill="none" stroke="#0b1f3b" stroke-width=".7"><path d="M1.5 3 5 1.5 8.5 3v4.5L5 9 1.5 7.5ZM1.5 3 5 4.5 8.5 3M5 4.5V9"/></svg>Materials Testing</li>
    <li style="left:128px;top:90px;width:110px"><svg viewBox="0 0 10 10" fill="none" stroke="#0b1f3b" stroke-width=".7"><circle cx="5" cy="5" r="1.5"/><circle cx="5" cy="5" r="3.2" stroke-dasharray="1.2 .8"/></svg>Mechanical Testing</li>
    <li style="left:128px;top:109px;width:110px"><svg viewBox="0 0 10 10" fill="none" stroke="#0b1f3b" stroke-width=".7"><path d="M2.5 7.5h5a2 2 0 0 0 0-4 2.5 2.5 0 0 0-4.8.5A1.8 1.8 0 0 0 2.5 7.5Z"/><circle cx="7.5" cy="7.5" r="1.2" stroke="#29aae2"/></svg>Nondestructive Testing (NDT)</li>
    <li style="left:128px;top:127px;width:110px"><svg viewBox="0 0 10 10" fill="none" stroke="#0b1f3b" stroke-width=".7"><circle cx="4.3" cy="4.3" r="3"/><path d="m6.5 6.5 2.5 2.5"/><path d="M3 4.5 4 5.5 5.8 3.3" stroke="#29aae2"/></svg>Failure Analysis</li>
    <li style="left:128px;top:146px;width:110px;border-bottom:none"><svg viewBox="0 0 10 10" fill="none" stroke="#0b1f3b" stroke-width=".7"><circle cx="5" cy="5" r="3.8" stroke-dasharray="1.5 .6"/><path d="M3.3 5 4.5 6.2 6.8 3.8"/></svg>Inspection &amp; Compliance Verification</li>
  </ul>
  <div class="vline" style="left:124px;top:70px;height:90px"></div>
  <p class="note" style="left:28px;top:175px">Every project is executed with precision, efficiency, and<br>internationally recognized quality standards.</p>
</section>

<!-- 04 Training -->
<section class="slide dark" style="left:90px;top:709px;width:362px;height:203px">
  <div class="abs" style="inset:0;background:linear-gradient(120deg,#0c2348 0%,#103262 55%,#0b2550 100%)" role="img" aria-label="Faint background photo of technicians training with rope access equipment"></div>
  <div class="badge" style="left:24px">04</div>
  <h2 class="title" style="left:24px;top:28px;color:var(--white)">TRAINING &amp; CERTIFICATION</h2>
  <p class="subtitle" style="left:24px;top:47px">Building Skills. Ensuring Safety.<br>Advancing Careers.</p>
  <p class="body" style="left:24px;top:88px;width:110px;color:#dfe6ef;text-align:justify">Gain practical skills through industry-focused programs designed to improve safety, compliance, and operational excellence</p>
  <p class="body" style="left:24px;top:111px;width:110px;color:#dfe6ef;text-align:justify">Our programs comply with applicable industry standards and combine expert instruction with practical, hands-on learning-equipping students with the knowledge and know-how to enhance safety, efficiency, and reliability.</p>
  <div class="vline" style="left:168px;top:71px;height:94px;background:#4e6488"></div>
  <svg class="art" style="left:190px;top:55px" width="130" height="115" viewBox="0 0 130 115" fill="none" stroke="var(--blue-strong)" stroke-width="1.8">
    <polygon points="72,2 100,2 114,31 100,60 72,60 58,31"/>
    <polygon points="28,31 56,31 70,60 56,89 28,89 14,60"/>
    <polygon points="72,60 100,60 114,89 100,118 72,118 58,89" transform="translate(0,-4)"/>
    <text class="hexlabel" x="86" y="29" stroke="none">ROPE</text>
    <text class="hexlabel" x="86" y="37" stroke="none">ACCESS</text>
    <text class="hexlabel" x="42" y="58" stroke="none">NONDESTRUCTIVE</text>
    <text class="hexlabel" x="42" y="66" stroke="none">TESTING (NDT)</text>
    <text class="hexlabel" x="86" y="86" stroke="none">RELIABILITY</text>
    <text class="hexlabel" x="86" y="94" stroke="none">TRAINING</text>
  </svg>
  <div class="location">LOCATION</div>
  <div class="loc-item" style="left:100px">
    <svg width="8" height="8" viewBox="0 0 8 8" fill="none" stroke="#fff" stroke-width=".7"><rect x=".5" y="1" width="6" height="4.5"/><path d="M2 7.5h3M3.5 5.5v2"/></svg>
    <span><small>In-person</small>Riverton, GA</span>
  </div>
  <div class="loc-item" style="left:165px;top:171px">
    <svg width="9" height="9" viewBox="0 0 9 9" fill="none" stroke="#fff" stroke-width=".8"><circle cx="4.5" cy="4.5" r="3.7"/><path d="M1 4.5h7M4.5 1c-2 2-2 5 0 7"/></svg>
    <span>Online</span>
  </div>
</section>

<!-- 05 Industries -->
<section class="slide" style="left:472px;top:709px;width:362px;height:203px">
  <svg class="art" style="left:0;top:0" width="362" height="203" viewBox="0 0 362 203">
    <polygon points="280,0 362,0 362,82" fill="#e3e7ec"/>
    <polygon points="288,0 362,0 362,74" fill="var(--blue-strong)"/>
  </svg>
  <div class="badge" style="left:28px">05</div>
  <h2 class="title" style="left:27px;top:29px">INDUSTRIES WE SERVE</h2>
  <p class="subtitle" style="left:27px;top:46px">Supporting Critical Industries Worldwide</p>
  <div class="accent" style="left:27px;top:68px;width:33px"></div>
  <div class="industry" style="left:20px;top:79px"><svg viewBox="0 0 17 17" fill="none" stroke="#0b1f3b" stroke-width=".8"><path d="M1 9h15M9 9 5 3h2l5 6M9 9l-4 6h2l5-6M2 9 1 6h1.5l2 3"/></svg>Aerospace &amp;<br>Aviation</div>
  <div class="industry" style="left:69px;top:79px"><svg viewBox="0 0 17 17" fill="none" stroke="#0b1f3b" stroke-width=".8"><path d="M2 11V8l2-4h9l2 4v3Z"/><circle cx="5" cy="12" r="1.5"/><circle cx="12" cy="12" r="1.5"/></svg>Automotive</div>
  <div class="industry" style="left:117px;top:79px"><svg viewBox="0 0 17 17" fill="none" stroke="#0b1f3b" stroke-width=".8"><path d="M3 15V6h3v9M7 15V3h3v12M11 15V8h3v7M2 15h13"/></svg>Chemical</div>
  <div class="industry" style="left:167px;top:79px"><svg viewBox="0 0 17 17" fill="none" stroke="#0b1f3b" stroke-width=".8"><path d="M6 16V2M8 16V2M2 4h14M14 4v5M3 16h8"/></svg>Construction</div>
  <div class="industry" style="left:214px;top:79px"><svg viewBox="0 0 17 17" fill="none" stroke="#0b1f3b" stroke-width=".8"><path d="M8.5 1 15 3.5V8c0 4-6.5 7.5-6.5 7.5S2 12 2 8V3.5Z"/><path d="M5 6l7 5M5 11l7-5" stroke="#29aae2"/></svg>Defense</div>
  <div class="industry" style="left:263px;top:79px"><svg viewBox="0 0 17 17" fill="none" stroke="#0b1f3b" stroke-width=".8"><circle cx="11" cy="5" r="2.5" stroke="#29aae2"/><path d="M11 0v1M11 9v1M6 5h1M15 5h1"/><rect x="2" y="10" width="6" height="5"/></svg>Energy Storage</div>
  <div class="industry" style="left:20px;top:121px"><svg viewBox="0 0 17 17" fill="none" stroke="#0b1f3b" stroke-width=".8"><rect x="2" y="4" width="11" height="10"/><path d="M7.5 6.5v5M5 9h5" stroke="#29aae2"/></svg>Healthcare &amp;<br>Life Sciences</div>
  <div class="industry" style="left:69px;top:121px"><svg viewBox="0 0 17 17" fill="none" stroke="#0b1f3b" stroke-width=".8"><path d="M2 15V8l4-3v3l4-3v3l4-3v10Z"/><path d="M11 5V1h2v4"/></svg>Manufacturing</div>
  <div class="industry" style="left:117px;top:121px"><svg viewBox="0 0 17 17" fill="none" stroke="#0b1f3b" stroke-width=".8"><path d="M1 5l8-3 5 3M5 4v11M9 15l3-10 3 10M10.5 10h3"/></svg>Oil &amp; Gas</div>
  <div class="industry" style="left:167px;top:121px"><svg viewBox="0 0 17 17" fill="none" stroke="#0b1f3b" stroke-width=".8"><path d="M8.5 6 5 16M8.5 6 12 16M6 12h5"/><circle cx="8.5" cy="5" r="1.2"/><path d="M5 2a5 5 0 0 0 0 6M12 2a5 5 0 0 1 0 6" stroke="#29aae2"/></svg>Telecommunications</div>
  <div class="industry" style="left:214px;top:121px"><svg viewBox="0 0 17 17" fill="none" stroke="#0b1f3b" stroke-width=".8"><path d="M8.5 2v13M4 15h9M2 4h13M4 4 2 9h4ZM13 4l-2 5h4Z"/></svg>Insurance<br>&amp; Legal</div>
  <div class="industry" style="left:263px;top:121px"><svg viewBox="0 0 17 17" fill="none" stroke="#0b1f3b" stroke-width=".8"><ellipse cx="9" cy="3" rx="4" ry="2" stroke="#29aae2"/><path d="M2 16V8h4v2l3-2v2l3-2v8Z"/></svg>Pulp &amp; Paper</div>
  <div class="vline" style="left:67px;top:82px;height:22px"></div><div class="vline" style="left:115px;top:82px;height:22px"></div>
  <div class="vline" style="left:165px;top:82px;height:22px"></div><div class="vline" style="left:213px;top:82px;height:22px"></div>
  <div class="vline" style="left:262px;top:82px;height:22px"></div>
  <div class="vline" style="left:67px;top:124px;height:22px"></div><div class="vline" style="left:115px;top:124px;height:22px"></div>
  <div class="vline" style="left:165px;top:124px;height:22px"></div><div class="vline" style="left:213px;top:124px;height:22px"></div>
  <div class="vline" style="left:262px;top:124px;height:22px"></div>
  <p class="note" style="left:27px;top:173px;font-size:6px;font-weight:400">No matter the industry, we help clients<br>minimize risk and maximize performance.</p>
  <div class="dots" style="left:292px;top:178px"></div>
</section>

<!-- 06 Why clients choose us -->
<section class="slide" style="left:90px;top:929px;width:362px;height:203px">
  <svg class="art" style="left:0;top:0" width="362" height="203" viewBox="0 0 362 203">
    <defs>
      <radialGradient id="globePhoto" cx=".6" cy=".45" r=".7">
        <stop offset="0" stop-color="#4a68c8"/><stop offset=".5" stop-color="#1c2f7a"/><stop offset="1" stop-color="#070f33"/>
      </radialGradient>
    </defs>
    <polygon points="262,0 362,0 362,203 283,203 216,98" fill="#e3e7ec"/>
    <polygon points="267,0 362,0 362,203 288,203 222,98" fill="url(#globePhoto)" role="img" aria-label="Photo of a glowing earth wrapped in a network of connection lines"/>
    <polygon points="215,203 288,203 288,160 260,160" fill="var(--blue-strong)"/>
  </svg>
  <div class="badge" style="left:29px">06</div>
  <h2 class="title" style="left:28px;top:29px">WHY CLIENTS CHOOSE US</h2>
  <p class="subtitle" style="left:28px;top:46px">Confidence Through Partnership</p>
  <div class="reason" style="top:68px;width:99px"><svg viewBox="0 0 13 13"><circle cx="6.5" cy="6.5" r="6" fill="var(--navy)"/><path d="M6.5 9.5 3.8 7a1.5 1.5 0 0 1 2.7-2 1.5 1.5 0 0 1 2.7 2Z" fill="none" stroke="#fff" stroke-width=".6"/></svg><div><h3>Trust &amp; Independence</h3><p>Objective testing and transparent<br>reporting you can rely on.</p></div></div>
  <div class="reason" style="top:94px;width:99px"><svg viewBox="0 0 13 13"><circle cx="6.5" cy="6.5" r="6" fill="var(--navy)"/><circle cx="6.5" cy="6.5" r="3" fill="none" stroke="#fff" stroke-width=".6"/><circle cx="6.5" cy="6.5" r=".9" fill="#fff"/></svg><div><h3>Technical Accuracy</h3><p>Highly skilled specialists using advanced<br>methodologies and equipment.</p></div></div>
  <div class="reason" style="top:121px;width:99px"><svg viewBox="0 0 13 13"><circle cx="6.5" cy="6.5" r="6" fill="var(--navy)"/><circle cx="6.5" cy="7" r="3" fill="none" stroke="#fff" stroke-width=".6"/><path d="M6.5 7V5.2M5.5 3.3h2" stroke="#fff" stroke-width=".6"/></svg><div><h3>Fast Turnaround</h3><p>Efficient processes that keep projects<br>moving and reduce downtime.</p></div></div>
  <div class="reason" style="top:147px;width:99px"><svg viewBox="0 0 13 13"><circle cx="6.5" cy="6.5" r="6" fill="var(--navy)"/><path d="M4 9.5V7.5M6 9.5V6M8 9.5V4.5M3.5 5.5 8.5 3" stroke="#fff" stroke-width=".6"/></svg><div><h3>Value Beyond Compliance</h3><p>Actionable insights that improve quality,<br>performance, and long-term reliability.</p></div></div>
  <div class="reason" style="top:173px;border-bottom:none"><svg viewBox="0 0 13 13"><circle cx="6.5" cy="6.5" r="6" fill="var(--navy)"/><circle cx="6.5" cy="6.5" r="3.2" fill="none" stroke="#fff" stroke-width=".6"/><path d="M3.3 6.5h6.4M6.5 3.3c-1.5 2-1.5 4.4 0 6.4" fill="none" stroke="#fff" stroke-width=".5"/></svg><div><h3>Global Reach</h3><p>Serving organizations across the United States and<br>international markets with consistent, dependable expertise.</p></div></div>
</section>

<!-- 07 Closing -->
<section class="slide" style="left:472px;top:929px;width:362px;height:203px">
  <svg class="art" style="left:0;top:0" width="362" height="203" viewBox="0 0 362 203">
    <defs>
      <linearGradient id="handshakePhoto" x1="0" y1="0" x2="1" y2="1">
        <stop offset="0" stop-color="#1d3a66"/><stop offset=".55" stop-color="#8fa4bf"/><stop offset="1" stop-color="#dfe6ee"/>
      </linearGradient>
    </defs>
    <polygon points="204,0 362,0 362,203 275,203" fill="#e3e7ec"/>
    <polygon points="210,0 362,0 362,203 281,203" fill="url(#handshakePhoto)" role="img" aria-label="Photo of two business professionals shaking hands"/>
    <polygon points="250,203 362,203 362,120" fill="var(--blue-strong)"/>
  </svg>
  <div class="badge" style="left:25px">07</div>
  <h2 class="title" style="left:24px;top:29px;font-size:16.5px;line-height:1.12">LET'S BUILD<br>CONFIDENCE<br><span style="color:var(--blue-strong)">TOGETHER</span></h2>
  <div class="accent" style="left:24px;top:91px;width:33px"></div>
  <p class="body" style="left:24px;top:99px;width:122px">Whether validating products, ensuring regulatory compliance, investigating failures, or improving operational reliability, we provide the expertise and responsiveness needed to help you succeed.</p>
  <div class="benefit" style="left:16px"><svg viewBox="0 0 14 14" fill="none" stroke="#0b1f3b" stroke-width=".8"><rect x="2" y="2.5" width="10" height="10" rx="1"/><path d="M4.5 7.5 6.3 9.3 9.5 5.5" stroke="#29aae2"/></svg>Reliable Results</div>
  <div class="benefit" style="left:73px"><svg viewBox="0 0 14 14" fill="none" stroke="#0b1f3b" stroke-width=".8"><circle cx="7" cy="7" r="5.5"/><path d="M7 4v3.5l2 1.5" stroke="#29aae2"/></svg>Faster Decisions</div>
  <div class="benefit" style="left:130px"><svg viewBox="0 0 14 14" fill="none" stroke="#0b1f3b" stroke-width=".8"><path d="M7 2 13 12.5H1Z"/><path d="M7 6v3.2M7 10.5v.6" stroke="#29aae2"/></svg>Reduced Risk</div>
  <div class="benefit" style="left:190px"><svg viewBox="0 0 14 14" fill="none" stroke="#0b1f3b" stroke-width=".8"><path d="M2.5 8V6.5a4.5 4.5 0 0 1 9 0V8"/><rect x="1.8" y="7.5" width="2" height="3.5" rx=".8"/><rect x="10.2" y="7.5" width="2" height="3.5" rx=".8"/></svg>Long-Term<br>Technical Support</div>
  <div class="vline" style="left:71px;top:142px;height:24px"></div>
  <div class="vline" style="left:128px;top:142px;height:24px"></div>
  <div class="vline" style="left:186px;top:142px;height:24px"></div>
  <div class="contact-edge"></div>
  <div class="contact">CONTACT US</div>
  <div class="contact-item" style="left:100px">
    <svg width="11" height="11" viewBox="0 0 11 11" fill="none" stroke="#0b1f3b" stroke-width=".7"><circle cx="5.5" cy="5.5" r="4.8"/><path d="M.7 5.5h9.6M5.5.7c-2.3 2.6-2.3 7 0 9.6M5.5.7c2.3 2.6 2.3 7 0 9.6"/></svg>
    <span><small>Website:</small>qirvotest.com</span>
  </div>
  <div class="contact-item" style="left:163px">
    <svg width="9" height="9" viewBox="0 0 9 9" fill="none" stroke="#0b1f3b" stroke-width=".7"><rect x=".5" y=".5" width="8" height="8"/><path d="M2.5 2.2c0 2.5 1.8 4.3 4.3 4.3l.2-1.2-1.2-.6-.6.6c-.8-.4-1.3-.9-1.7-1.7l.6-.6-.6-1.2Z"/></svg>
    <span><small>Phone</small>+1 (888) 555-0142</span>
  </div>
</section>

</body>
</html>
```